R & T Welford Carpet & Gutter Cleaning

We clean carpets and have an environmentally friendly gutter machine that cleans out the guttering leaving no mess
Phone 0402718395
or 0413862047

Industry/Entity Type

Business

```html
<!DOCTYPE html>
<html lang="en">
<head>
<meta charset="utf-8">
<title>R &amp; T Welford Carpet &amp; Gutter Cleaning – Business Card</title>
<link rel="stylesheet" href="https://fonts.googleapis.com/css2?family=Michroma&family=Archivo:wght@800&family=Roboto:wght@400;500&display=swap">
<style>
  :root {
    --bg: #ecebe8;
    --blue: #0fa9e6;
    --slate: #6b6c6e;
    --charcoal: #3a3b3d;
    --white: #ffffff;
    --ink: #1f1f21;
  }
  * { box-sizing: border-box; margin: 0; padding: 0; }
  html, body { width: 1200px; height: 1050px; overflow: hidden; background: var(--bg); }
  .canvas { position: relative; width: 1200px; height: 1050px; }

  .card {
    position: absolute;
    top: 175px;
    width: 400px;
    height: 700px;
    overflow: hidden;
    box-shadow: 0 10px 30px rgba(0,0,0,.18);
  }
  .card--front { left: 150px; background: var(--slate); }
  .card--back { left: 650px; background: var(--white); }

  /* front header */
  .front-header {
    position: absolute; left: 0; top: 0; width: 100%; height: 158px;
    background: var(--white);
    border-top: 7px solid var(--blue);
    border-bottom: 8px solid var(--blue);
    display: flex; align-items: center; justify-content: center;
  }
  .business-name {
    font-family: "Roboto", sans-serif;
    font-weight: 500;
    font-size: 22px;
    line-height: 1.35;
    color: var(--ink);
    text-align: center;
  }

  .connector-lines { position: absolute; left: 0; top: 158px; }

  .name-box {
    position: absolute; left: 165px; top: 188px; width: 215px; height: 68px;
    background: var(--white); text-align: center; padding-top: 12px;
  }
  .person-name {
    font-family: "Archivo", sans-serif; font-weight: 800;
    font-size: 22px; color: var(--ink); letter-spacing: .5px;
  }
  .person-role {
    font-family: "Roboto", sans-serif; font-size: 12.5px; color: var(--ink); margin-top: 3px;
  }

  .contact-box {
    position: absolute; left: 125px; width: 245px; height: 60px;
    border: 2px solid var(--white); text-align: center; padding-top: 8px; color: var(--white);
  }
  .contact-box--phone { top: 292px; }
  .contact-box--email { top: 374px; }
  .contact-box--web { top: 456px; }
  .contact-label {
    font-family: "Archivo", sans-serif; font-weight: 800; font-size: 16px; letter-spacing: .5px;
  }
  .contact-value {
    font-family: "Roboto", sans-serif; font-size: 13px; margin-top: 4px; letter-spacing: .5px;
  }

  .front-rule { position: absolute; left: 0; top: 552px; width: 100%; height: 10px; background: var(--charcoal); }
  .front-footer {
    position: absolute; left: 0; top: 562px; width: 100%; height: 138px;
    background: var(--blue); padding: 34px 24px 0;
  }
  .address {
    font-family: "Michroma", sans-serif; font-size: 13.5px; color: var(--white); line-height: 1.9;
  }

  /* back */
  .back-rule { position: absolute; left: 0; top: 330px; width: 100%; height: 14px; background: var(--charcoal); }
  .back-footer {
    position: absolute; left: 0; top: 344px; width: 100%; height: 356px;
    background: var(--blue); padding: 70px 40px 0;
  }
  .back-footer .address { font-size: 16px; line-height: 2.1; }
</style>
</head>
<body>
<main class="canvas">

  <section class="card card--front" aria-label="Business card front">
    <header class="front-header">
      <p class="business-name">R &amp; T Welford<br>Carpet &amp; Gutter Cleaning</p>
    </header>

    <svg class="connector-lines" width="400" height="400" viewBox="0 0 400 400" aria-hidden="true">
      <g fill="none" stroke="#ffffff" stroke-width="2">
        <polyline points="165,42 70,42 70,100 40,100 40,362 125,362"/>
        <line x1="40" y1="164" x2="125" y2="164"/>
        <line x1="40" y1="246" x2="125" y2="246"/>
      </g>
    </svg>

    <div class="name-box">
      <div class="person-name">DANIEL ROAKE</div>
      <div class="person-role">Managing Director</div>
    </div>

    <div class="contact-box contact-box--phone">
      <div class="contact-label">PHONE</div>
      <div class="contact-value">0402718395</div>
    </div>
    <div class="contact-box contact-box--email">
      <div class="contact-label">EMAIL</div>
      <div class="contact-value">hello@rtwelford.com</div>
    </div>
    <div class="contact-box contact-box--web">
      <div class="contact-label">WEBSITE</div>
      <div class="contact-value">www.rtwelfordcleaning.com</div>
    </div>

    <div class="front-rule"></div>
    <footer class="front-footer">
      <p class="address">Unit 4, 27 Harbour Road Kelso</p>
    </footer>
  </section>

  <section class="card card--back" aria-label="Business card back">
    <div class="back-rule"></div>
    <footer class="back-footer">
      <p class="address">Unit 4, 27 Harbour Road<br>Kelso</p>
    </footer>
  </section>

</main>
</body>
</html>
```